Seeking A Captivating Design For Meditation Ebook

I'm looking for a creative and Captivating design for my meditation ebook. The design will have to be in a 3D design mockup as well as provide a 2D version of the book.

My website is quietharborpages.com/ebook

The design should blend in with the page. Some ideas are to put an ocean or maybe a sky. It should be calming. It should have some orange in there as well to blend with the page. I'm open to other ideas as well.

The title of the book should say, Stillwater Morning Path as the main headline. The sub headline will say, "How to eliminate depression one breath at a time" and the author name will be in small letters that says, Dwight Hallam

Font styles to use
Serif

Colors

Designer to choose colors to be used in the design.

Requirements
Must have
• Some type of orange color. Something calming like an ocean or a sky or a forest or someone meditating
Nice to have
• Maybe an ocean, sky, forest, person meditating, maybe some orange letters. I like the color blue as well
Should not have
• Any red.

```html
<!DOCTYPE html>
<html lang="en">
<head>
<meta charset="UTF-8">
<title>Stillwater Morning Path — Cover</title>
<link rel="stylesheet" href="https://fonts.googleapis.com/css2?family=Macondo&family=Lora:ital,wght@0,400;1,400&display=swap">
<style>
  :root {
    --page-bg: #e6dccd;
    --photo-top: #e9bd7e;
    --photo-mid: #efb04a;
    --photo-low: #b8651f;
    --photo-base: #2e1c12;
    --title: #d76f1c;
    --title-edge: #f7dcb0;
    --subtitle: #8a4210;
    --author: #f3d9b0;
  }
  * { margin: 0; padding: 0; box-sizing: border-box; }
  html, body {
    width: 1200px;
    height: 789px;
    overflow: hidden;
    background: var(--page-bg);
  }
  .canvas {
    width: 1200px;
    height: 789px;
    display: flex;
    align-items: center;
    justify-content: center;
  }
  .book-cover {
    position: relative;
    width: 436px;
    height: 729px;
    overflow: hidden;
    box-shadow: 0 6px 18px rgba(60, 40, 20, 0.18);
  }
  .cover-photo {
    position: absolute;
    inset: 0;
    background: linear-gradient(180deg, var(--photo-top) 0%, var(--photo-mid) 45%, var(--photo-low) 78%, var(--photo-base) 100%);
  }
  .cover-title {
    position: absolute;
    left: 36px;
    top: 78px;
    font-family: "Macondo", cursive;
    font-weight: 400;
    color: var(--title);
    text-shadow: 1px 1px 0 var(--title-edge);
    transform: rotate(-5deg);
    transform-origin: left top;
    line-height: 1;
    white-space: nowrap;
  }
  .cover-title__line {
    display: block;
    font-size: 54px;
  }
  .cover-title__line--second {
    margin-left: 56px;
    margin-top: 6px;
  }
  .cover-subtitle {
    position: absolute;
    left: 40px;
    right: 40px;
    top: 232px;
    font-family: "Lora", serif;
    font-style: italic;
    font-size: 17px;
    line-height: 1.4;
    color: var(--subtitle);
  }
  .cover-author {
    position: absolute;
    left: 0;
    right: 0;
    bottom: 34px;
    text-align: center;
    font-family: "Lora", serif;
    font-size: 14px;
    letter-spacing: 3px;
    text-transform: uppercase;
    color: var(--author);
  }
</style>
</head>
<body>
  <main class="canvas">
    <article class="book-cover">
      <div class="cover-photo" role="img" aria-label="Photograph of a golden sunset sky over dark hills, with a person seated in a meditation pose in silhouette on a rock at the right"></div>
      <h1 class="cover-title">
        <span class="cover-title__line">Stillwater</span>
        <span class="cover-title__line cover-title__line--second">Morning Path</span>
      </h1>
      <p class="cover-subtitle">How to eliminate depression one breath at a time</p>
      <p class="cover-author">Dwight Hallam</p>
    </article>
  </main>
</body>
</html>
```